" A proprietária é a Lorena Bastolli, Biomedica, pós graduada em estética e Mestra pela Universidade de Vale Dourado. Temos trabalhando conosco uma fisioterapeuta, uma esteticista, uma estagiária em biomedica, uma secretária, e temos parceria com uma Nutricionista com PHD e uma Médica especialista em Endocrinologia, ambas atendem na clínica uma vez por semana. "

```html
<!DOCTYPE html>
<html lang="pt-BR">
<head>
<meta charset="UTF-8">
<title>Lorena Bastolli — Papel timbrado</title>
<link rel="stylesheet" href="https://fonts.googleapis.com/css2?family=Gilda+Display&family=Montserrat:wght@400;500&display=swap">
<style>
  :root {
    --backdrop: #e6e6e6;
    --paper: #ffffff;
    --ink: #4a4a4a;
    --ink-soft: #7a7a7a;
    --gold: #c9a25a;
    --pattern: #f1f1f1;
  }
  html, body {
    margin: 0;
    width: 1200px;
    height: 1200px;
    overflow: hidden;
    background: var(--backdrop);
  }
  .letterhead {
    position: absolute;
    left: 211px;
    top: 50px;
    width: 778px;
    height: 1100px;
    background: var(--paper);
    box-shadow: 0 4px 18px rgba(0,0,0,0.08);
  }
  .pattern-top {
    position: absolute;
    left: 40px;
    right: 60px;
    top: 58px;
    height: 56px;
    background: linear-gradient(90deg, rgba(241,241,241,0) 0%, var(--pattern) 25%, var(--pattern) 100%);
  }
  .pattern-right {
    position: absolute;
    right: 60px;
    top: 58px;
    width: 56px;
    height: 760px;
    background: linear-gradient(180deg, var(--pattern) 0%, var(--pattern) 75%, rgba(241,241,241,0) 100%);
  }
  .brand-mark {
    position: absolute;
    right: 92px;
    top: 40px;
    width: 46px;
    height: 46px;
    border-radius: 50%;
    background: var(--gold);
  }
  .brand-name {
    position: absolute;
    right: 70px;
    bottom: 110px;
    text-align: right;
    font-family: "Gilda Display", serif;
    color: var(--ink);
    font-size: 40px;
    line-height: 1.02;
  }
  .brand-tagline {
    display: block;
    margin-top: 8px;
    font-family: "Montserrat", sans-serif;
    font-size: 10px;
    letter-spacing: 3px;
    text-transform: uppercase;
    color: var(--ink-soft);
  }
  .contact {
    position: absolute;
    left: 60px;
    bottom: 70px;
    margin: 0;
    padding: 0;
    list-style: none;
    font-family: "Montserrat", sans-serif;
    font-size: 12px;
    color: var(--ink);
  }
  .contact li {
    display: flex;
    align-items: flex-start;
    gap: 8px;
    margin-top: 10px;
    line-height: 1.35;
  }
  .contact svg { flex: none; margin-top: 1px; }
  .contact .dot {
    flex: none;
    width: 11px;
    height: 11px;
    margin-top: 2px;
    border-radius: 50%;
    background: var(--gold);
  }
</style>
</head>
<body>
  <main class="letterhead">
    <div class="pattern-top" role="img" aria-label="Faixa decorativa suave de flores ao longo do topo"></div>
    <div class="pattern-right" role="img" aria-label="Faixa decorativa suave de flores ao longo da margem direita"></div>
    <div class="brand-mark" aria-hidden="true"></div>

    <div class="brand-name">Lorena<br>Bastolli
      <span class="brand-tagline">Biomedicina Estética</span>
    </div>

    <ul class="contact">
      <li>
        <svg width="12" height="12" viewBox="0 0 24 24" aria-hidden="true"><path fill="#c9a25a" d="M6.6 10.8a15 15 0 0 0 6.6 6.6l2.2-2.2c.3-.3.7-.4 1-.2 1.1.4 2.3.6 3.6.6.6 0 1 .4 1 1V20c0 .6-.4 1-1 1A17 17 0 0 1 3 4c0-.6.4-1 1-1h3.5c.6 0 1 .4 1 1 0 1.3.2 2.5.6 3.6.1.3 0 .7-.2 1z"/></svg>
        <span>+55 (16) 98123-4567</span>
      </li>
      <li>
        <svg width="12" height="14" viewBox="0 0 24 28" aria-hidden="true"><path fill="#c9a25a" d="M12 0a9 9 0 0 0-9 9c0 7 9 19 9 19s9-12 9-19a9 9 0 0 0-9-9zm0 12.5A3.5 3.5 0 1 1 12 5.5a3.5 3.5 0 0 1 0 7z"/></svg>
        <span>Rua das Acácias, 1280<br>Franca - SP</span>
      </li>
      <li>
        <span class="dot" aria-hidden="true"></span>
        <span>@lorenabastolli</span>
      </li>
      <li>
        <svg width="12" height="12" viewBox="0 0 24 24" aria-hidden="true"><circle cx="12" cy="12" r="10" fill="none" stroke="#c9a25a" stroke-width="2"/><path d="M2 12h20M12 2c3 3 3 17 0 20M12 2c-3 3-3 17 0 20" fill="none" stroke="#c9a25a" stroke-width="1.6"/></svg>
        <span>www.lorenabastolli.com.br</span>
      </li>
    </ul>
  </main>
</body>
</html>
```